Business Card Design Project

Keep it simple , using logo and colors that compliment. Logo on one side with complimentary back ground color. Other side, personal info with possible complimentary design/colors

Target Market(s)

we are a non for profit that will be seeking donations . Both monetary and in kind

Industry/Entity Type

Business

Font styles to use
Sans Serif

Colors

Designer to choose colors to be used in the design.

```html
<!DOCTYPE html>
<html lang="en">
<head>
<meta charset="utf-8">
<title>Bright Steps Fund – Business Card</title>
<link href="https://fonts.googleapis.com/css2?family=Open+Sans:wght@300;400;700&display=swap" rel="stylesheet">
<style>
  :root {
    --navy: #2b2f4e;
    --yellow: #f0d400;
    --ink-light: #d9dbe6;
    --ink-muted: #b9bccb;
    --backdrop: #e6e6e6;
  }
  * { box-sizing: border-box; margin: 0; padding: 0; }
  html, body {
    width: 1200px;
    height: 675px;
    overflow: hidden;
    background: var(--backdrop);
    font-family: "Open Sans", Arial, sans-serif;
  }
  .canvas {
    width: 1200px;
    height: 675px;
    display: flex;
    align-items: center;
    justify-content: center;
    gap: 60px;
  }
  .card {
    position: relative;
    width: 520px;
    height: 297px;
    background: var(--navy);
    overflow: hidden;
  }

  /* Organisation name */
  .brand-name {
    color: var(--yellow);
    font-weight: 300;
    white-space: nowrap;
  }

  /* Front side */
  .card-front {
    display: flex;
    align-items: center;
    justify-content: center;
  }
  .card-front .brand-name { font-size: 36px; letter-spacing: 0.5px; }

  /* Back side */
  .card-back .brand-name {
    position: absolute;
    left: 34px;
    top: 134px;
    font-size: 19px;
  }

  .contact {
    position: absolute;
    left: 268px;
    top: 88px;
    color: var(--ink-light);
  }
  .contact-name {
    color: var(--yellow);
    font-weight: 700;
    font-size: 15px;
    line-height: 1.2;
  }
  .contact-role {
    font-size: 9.5px;
    color: var(--ink-muted);
    margin-bottom: 14px;
  }
  .contact-list { list-style: none; }
  .contact-item {
    display: flex;
    align-items: center;
    gap: 8px;
    font-size: 11.5px;
    line-height: 1;
    margin-bottom: 7px;
  }
  .contact-item .icon {
    width: 11px;
    height: 11px;
    fill: var(--yellow);
    flex: none;
  }
  .contact-item .icon-line {
    fill: none;
    stroke: var(--yellow);
    stroke-width: 1.3;
  }
  .contact-split { margin-left: 10px; display: inline-flex; align-items: center; gap: 6px; }

  .accent-band {
    position: absolute;
    left: 0;
    right: 0;
    bottom: 0;
    height: 9px;
    background: var(--yellow);
  }
</style>
</head>
<body>
<main class="canvas">

  <section class="card card-front" aria-label="Card front">
    <span class="brand-name">Bright Steps Fund</span>
  </section>

  <section class="card card-back" aria-label="Card back">
    <span class="brand-name">Bright Steps Fund</span>

    <div class="contact">
      <p class="contact-name">Your Long Name</p>
      <p class="contact-role">Owner / President</p>
      <ul class="contact-list">
        <li class="contact-item">
          <svg class="icon" viewBox="0 0 12 12" aria-hidden="true"><path fill-rule="evenodd" d="M6 0a4 4 0 0 0-4 4c0 3 4 8 4 8s4-5 4-8a4 4 0 0 0-4-4zm0 5.6A1.6 1.6 0 1 1 6 2.4a1.6 1.6 0 0 1 0 3.2z"/></svg>
          <span>Your Commercial or office address</span>
        </li>
        <li class="contact-item">
          <svg class="icon" viewBox="0 0 12 12" aria-hidden="true"><path d="M1 3c0-1 1-2 5-2s5 1 5 2v1H8V3H4v1H1zM3 5h6l2 6H1z"/></svg>
          <span>00.00.00.0000</span>
          <span class="contact-split">
            <svg class="icon" viewBox="0 0 12 12" aria-hidden="true"><path fill-rule="evenodd" d="M3 0h5v4H3zM1 4h10v7H1zm2 2v1h2V6zm4 0v1h2V6zM3 8v1h2V8zm4 0v1h2V8z"/></svg>
            <span>00.00.00.0000</span>
          </span>
        </li>
        <li class="contact-item">
          <svg class="icon" viewBox="0 0 12 12" aria-hidden="true"><path d="M0 2h12v1L6 7 0 3zm0 2.2 6 4 6-4V10H0z"/></svg>
          <span>yourname@yourwebsite.com</span>
        </li>
        <li class="contact-item">
          <svg class="icon icon-line" viewBox="0 0 12 12" aria-hidden="true"><circle cx="6" cy="6" r="5.2"/><ellipse cx="6" cy="6" rx="2.2" ry="5.2"/><path d="M0.8 6h10.4"/></svg>
          <span>www.yourwebsite.com</span>
        </li>
      </ul>
    </div>

    <div class="accent-band"></div>
  </section>

</main>
</body>
</html>
```